KT Crewing business card

Require business card which includes:
Company name: KT CREWING PTY LTD
Email: Mick@ktcrewing.com.au
Phone: 0431 556 208
ACN: 517 238 649

slogan: Onsite Auto Electrician Labour hire

Details and logo on top side
Logo only on bottom side

colour codes : #F15A29 , #939598

Target Market(s)

Western Australia mining sector

Industry/Entity Type

Mining

Contact Information for Business Card

Require business card which includes: Company name: KT CREWING PTY LTD Email: Mick@ktcrewing.com.au Phone: 0431 556 208 ACN: 517 238 649 slogan: Onsite Auto Electrician Labour hire Details and logo on top side Logo only on bottom side colour codes : #F15A29 , #939598

Colors
EE7325
F08F49
F5BC92
FAE3D3
FDF4ED

Requirements
Must have
• double sided

```html
<!DOCTYPE html>
<html lang="en">
<head>
<meta charset="utf-8">
<title>KT Crewing business card</title>
<link rel="stylesheet" href="https://fonts.googleapis.com/css2?family=Montserrat:wght@400;500;700;800&display=swap">
<style>
  :root {
    --brand-orange: #F15A29;
    --brand-grey: #939598;
    --card-white: #ffffff;
    --ink: #1f1f1f;
    --backdrop: #1c1c1d;
  }
  * { box-sizing: border-box; margin: 0; padding: 0; }
  html, body {
    width: 1200px;
    height: 900px;
    overflow: hidden;
    background: var(--backdrop);
    font-family: "Montserrat", sans-serif;
  }
  .sheet {
    position: relative;
    width: 1200px;
    height: 900px;
    display: flex;
    flex-direction: column;
    align-items: center;
    justify-content: center;
    gap: 34px;
  }
  .card {
    position: relative;
    width: 700px;
    height: 400px;
    border-radius: 26px;
    overflow: hidden;
  }
  /* Front side */
  .card--front { background: var(--card-white); }
  .card__swoosh {
    position: absolute;
    inset: 0;
    width: 100%;
    height: 100%;
  }
  .details {
    position: absolute;
    left: 52px;
    top: 46px;
    color: var(--ink);
  }
  .details__company {
    color: var(--brand-orange);
    font-weight: 800;
    font-size: 22px;
    letter-spacing: 0.2px;
  }
  .details__acn {
    font-size: 19px;
    font-weight: 500;
    margin-top: 4px;
  }
  .contact {
    list-style: none;
    margin-top: 44px;
    font-size: 19px;
    font-weight: 500;
    line-height: 1.45;
  }
  .contact__item { display: flex; align-items: center; gap: 10px; }
  .contact__icon { width: 18px; height: 18px; flex: none; }
  .wordmark {
    position: absolute;
    display: flex;
    align-items: center;
    gap: 14px;
    font-weight: 800;
    white-space: nowrap;
    line-height: 1;
  }
  .wordmark__square { display: block; flex: none; }
  .card--front .wordmark {
    right: 40px;
    top: 252px;
    font-size: 42px;
    color: var(--brand-orange);
  }
  .card--front .wordmark__square {
    width: 28px; height: 28px;
    background: var(--brand-grey);
  }
  /* Back side */
  .card--back {
    background: var(--brand-orange);
    display: flex;
    align-items: center;
    justify-content: center;
  }
  .card--back .wordmark {
    position: static;
    font-size: 72px;
    color: var(--card-white);
  }
  .card--back .wordmark__square {
    width: 46px; height: 46px;
    background: var(--card-white);
  }
</style>
</head>
<body>
<main class="sheet">
  <section class="card card--front" aria-label="Business card front">
    <svg class="card__swoosh" viewBox="0 0 700 400" preserveAspectRatio="none" aria-hidden="true">
      <path d="M0,232 C70,290 270,318 440,340 C550,355 620,375 670,400 L0,400 Z" fill="#939598"/>
      <path d="M0,250 C80,300 270,328 430,350 C530,364 590,382 615,400 L0,400 Z" fill="#F15A29"/>
    </svg>
    <div class="details">
      <h1 class="details__company">KT CREWING PTY LTD</h1>
      <p class="details__acn">ACN: 517 238 649</p>
      <ul class="contact">
        <li class="contact__item">
          <svg class="contact__icon" viewBox="0 0 20 20" aria-hidden="true">
            <path fill="#F15A29" d="M2,6 C2,3 5,2 10,2 C15,2 18,3 18,6 L18,8 L14,8 L13,6 L7,6 L6,8 L2,8 Z M5,9 L15,9 L17,17 L3,17 Z"/>
            <circle cx="10" cy="13" r="2.4" fill="#ffffff"/>
          </svg>
          <span>0431 556 208</span>
        </li>
        <li class="contact__item">
          <svg class="contact__icon" viewBox="0 0 20 20" aria-hidden="true">
            <rect x="1" y="4" width="18" height="12" fill="#F15A29"/>
            <path d="M1.5,4.5 L10,11 L18.5,4.5" fill="none" stroke="#ffffff" stroke-width="1.6"/>
          </svg>
          <span>Mick@ktcrewing.com.au</span>
        </li>
        <li class="contact__slogan">Onsite Auto Electrician Labour hire</li>
      </ul>
    </div>
    <div class="wordmark">
      <span class="wordmark__square" aria-hidden="true"></span>
      <span class="wordmark__name">KT Crewing</span>
    </div>
  </section>

  <section class="card card--back" aria-label="Business card back">
    <div class="wordmark">
      <span class="wordmark__square" aria-hidden="true"></span>
      <span class="wordmark__name">KT Crewing</span>
    </div>
  </section>
</main>
</body>
</html>
```